CD Cover Artwork for Classical Music Cover

We are about to launch 13 CDs online for digital downloads and require artwork for the accompanying CD covers. As the covers will not be printed, we only require web-optimized artwork. We are fine with one standard template that can be adapted for all the covers. The only differentiating factors will be the colour of the covers and the title information. We need to create a more progressive, eye-catching design than the below examples which we have been promoting through our website until now. You have full liberties to come up with whatever design you think is more appropriate and to use whatever fonts and juxtaposition of content and images as you see fit.
ARTIST INFORMATION: Marten Vollock was an American composer who lived and worked his entire life in New York City. He was a 1930 Brennholt graduate and studied composition with Edwin Marsk, Lou Benton, Thaddeus Pellworth and Oscar Bramley. In a 1947 competition, with Karl Obenfeld as one of three jurors, Vollock’s "Harvest Prelude" won First Prize. He produced a large body of work comprising hundreds of compositions across diverse musical genres ... From 2001 to early 2008, Marten Vollock’s music came to life through a unique collaboration with many of the finest musicians in St. Petersburg, Russia. Nearly all of Vollock’s musical repertoire was transcribed from their original manuscripts to electronic form. And dozens of recording sessions produced 13 CDs, including all his chambers works, many piano concertos and symphonies, and works for horn, flute, strings and woodwinds. This “musical discovery” was the brainchild of his late son, Daniel Vollock.
ARTIST WEBSITE: www.martenvollock-example.com
FACEBOOK PAGE: https://www.facebook-example.com/pages/Marten-Vollock-A-Hidden-Score-of-Western-Sound/918273645501928
ATTACHMENTS:
- A few images of Marten Vollock (young and old)
- List of CD information along with a visual representation of the information that should be included
Target Market(s)
Classical music lovers the world over
Industry/Entity Type
Electronic
Look and feel
Each slider illustrates characteristics of the customer's brand and the style your logo design should communicate.

```html
<!DOCTYPE html>
<html lang="en">
<head>
<meta charset="utf-8">
<title>Marten Vollock – Selected Chamber Works</title>
<link rel="stylesheet" href="https://fonts.googleapis.com/css2?family=Cinzel:wght@400&family=Cormorant+Garamond:ital,wght@0,500;1,600&family=Open+Sans:wght@400;600&display=swap">
<style>
  :root {
    --page: #ffffff;
    --cover-deep: #0b1420;
    --cover-shadow: #152436;
    --series-accent: #d9663f;
    --series-glow: #f0a37f;
    --photo-tone: #8fa3b8;
    --ink-light: #ffffff;
    --ink-dark: #101820;
    --panel: rgba(217, 102, 63, 0.9);
    --frame: #ffffff;
  }
  * { margin: 0; padding: 0; box-sizing: border-box; }
  html, body {
    width: 1200px; height: 800px; overflow: hidden;
    background: var(--page);
  }
  .album-cover {
    position: absolute; left: 258px; top: 58px;
    width: 684px; height: 684px;
    background: var(--cover-deep);
    overflow: hidden;
  }
  .portrait-elder {
    position: absolute; left: 250px; top: 150px;
    width: 434px; height: 534px;
    background:
      radial-gradient(ellipse 60% 45% at 55% 45%, var(--photo-tone) 0%, rgba(143,163,184,0.35) 45%, transparent 80%),
      linear-gradient(160deg, var(--cover-shadow) 0%, rgba(217,102,63,0.55) 100%);
  }
  .composer-name {
    position: absolute; left: 32px; top: 30px;
    font-family: 'Cinzel', serif; font-weight: 400;
    font-size: 54px; letter-spacing: 4px; line-height: 1;
    color: var(--ink-light); white-space: nowrap;
  }
  .life-dates {
    position: absolute; right: 32px; top: 94px;
    font-family: 'Cormorant Garamond', serif; font-weight: 500;
    font-size: 24px; letter-spacing: 2px; line-height: 1;
    color: var(--series-glow);
  }
  .tagline {
    position: absolute; right: 32px; top: 122px;
    font-family: 'Cormorant Garamond', serif; font-style: italic; font-weight: 600;
    font-size: 34px; line-height: 1;
    color: var(--ink-light); white-space: nowrap;
  }
  .portrait-young {
    position: absolute; left: 32px; top: 392px;
    width: 236px; height: 262px;
    border: 6px solid var(--frame);
    background: radial-gradient(ellipse 45% 40% at 50% 42%, #b9c5d2 0%, #6d8197 50%, var(--cover-shadow) 100%);
  }
  .release-info {
    position: absolute; left: 386px; top: 486px;
    width: 266px; height: 124px;
    background: var(--panel);
    padding: 12px 16px 0 0;
    text-align: right;
    font-family: 'Open Sans', sans-serif; font-weight: 400;
    font-size: 23px; line-height: 1.2;
    color: var(--ink-light);
  }
  .release-info .disc-number { font-weight: 600; }
  .publisher {
    position: absolute; left: 386px; top: 614px;
    width: 266px; height: 40px;
    background: var(--page);
    padding-right: 16px;
    text-align: right;
    font-family: 'Open Sans', sans-serif; font-weight: 400;
    font-size: 21px; line-height: 40px;
    color: var(--ink-dark); white-space: nowrap;
  }
</style>
</head>
<body>
  <main class="album-cover">
    <div class="portrait-elder" role="img" aria-label="Toned photograph of the elderly composer writing at a desk"></div>
    <h1 class="composer-name">MARTEN VOLLOCK</h1>
    <p class="life-dates">1905-1986</p>
    <p class="tagline">A hidden score of Western sound</p>
    <div class="portrait-young" role="img" aria-label="Portrait of the composer as a young man in a bow tie"></div>
    <div class="release-info">
      <p class="disc-number">CD01</p>
      <p>Selected</p>
      <p>Chamber Works</p>
    </div>
    <p class="publisher">Calloway Editions</p>
  </main>
</body>
</html>
```